Dermatology in Your Lane Logo and business card

We provide dermatological services to the community. This includes Assisted Living Facilities, nursing homes and to large cooperation, Health fairs etc. We provide a health care provider that travels to institutions, providing these services. All procedures and surgeries are done onsite in one of our state of the art mobile clinics. We provide services including, but not limited to; skin biopsies, skin surgeries , surgical procedures including skin cancer removal mole removal and treatment of various skin disorders. we bring mobile Dermatology to you.

Industry/Entity Type

Business

Contact Information for Business Card

Need Logo address phone number, email website

Logo Text

Dermatology in Your Lane

Logo styles of interest
Emblem Logo
Abstract Logo
Character Logo
Lettermark Logo
Requirements
Must have
• Marcus Penhale ARNP DN-C
• Medical Facilitator
• P. (407) 555-3194
• Fax (386) 555-7721

```html
<!DOCTYPE html>
<html lang="en">
<head>
<meta charset="utf-8">
<title>Dermatology in Your Lane — Business Card</title>
<link rel="stylesheet" href="https://fonts.googleapis.com/css2?family=Arimo:wght@400&display=swap">
<style>
  :root {
    --page-bg: #ffffff;
    --card-bg: #005d56;
    --brand-teal: #4ec8bf;
    --text-light: #ffffff;
    --glow: rgba(120, 200, 190, 0.20);
  }
  html, body {
    margin: 0;
    width: 1200px;
    height: 720px;
    overflow: hidden;
    background: var(--page-bg);
  }
  .business-card {
    position: absolute;
    left: 40px;
    top: 50px;
    width: 1121px;
    height: 619px;
    background: var(--card-bg);
    overflow: hidden;
    color: var(--text-light);
    font-family: "Arimo", sans-serif;
  }
  .card-glow {
    position: absolute;
    left: 420px;
    top: 400px;
    width: 520px;
    height: 260px;
    border-radius: 50%;
    background: radial-gradient(ellipse at center, var(--glow) 0%, rgba(120,200,190,0.07) 55%, rgba(120,200,190,0) 75%);
  }
  .brand {
    position: absolute;
    left: 0;
    right: 0;
    top: 200px;
    display: flex;
    align-items: center;
    justify-content: center;
    gap: 26px;
  }
  .brand-dot {
    width: 62px;
    height: 62px;
    border-radius: 50%;
    background: var(--brand-teal);
    flex: none;
  }
  .brand-name {
    margin: 0;
    font-size: 58px;
    font-weight: 400;
    line-height: 1;
    letter-spacing: 1px;
    color: var(--text-light);
  }
  .contact-person {
    position: absolute;
    left: 40px;
    top: 440px;
    width: 426px;
    text-align: center;
  }
  .person-name {
    margin: 0;
    font-size: 44px;
    letter-spacing: 1px;
    line-height: 1.1;
  }
  .person-credentials {
    margin: 4px 0 0;
    font-size: 22px;
    letter-spacing: 1px;
  }
  .person-role {
    margin: 6px 0 0;
    font-size: 26px;
    letter-spacing: 2px;
  }
  .contact-lines {
    position: absolute;
    left: 656px;
    top: 442px;
    width: 400px;
    text-align: center;
    font-size: 33px;
    letter-spacing: 2px;
  }
  .contact-lines p {
    margin: 0 0 20px;
  }
</style>
</head>
<body>
  <main class="business-card">
    <div class="card-glow" role="img" aria-label="Soft scattered translucent bubble pattern in pale teal"></div>

    <header class="brand">
      <span class="brand-dot"></span>
      <h1 class="brand-name">Dermatology in Your Lane</h1>
    </header>

    <section class="contact-person">
      <p class="person-name">MARCUS PENHALE</p>
      <p class="person-credentials">ARNP DN-C</p>
      <p class="person-role">MEDICAL FACILITATOR</p>
    </section>

    <section class="contact-lines">
      <p class="contact-phone">P. (407) 555-3194</p>
      <p class="contact-fax">Fax (386) 555-7721</p>
    </section>
  </main>
</body>
</html>
```